flyer for roofing advertising

Need a modern, bold, luxurious advertisement flyer for our roofing company. located in buffalo, ny. Big house with a intense roof design asphalt shingles. slogan is "Reliability starts at the top". Colors varies but want it to be modern. we will be handing these out when we are working in the area. phone number is 716-555-0147 for the NO K.W estimate. also our services are roofing, roof repairs, gutters, attic ventilation. we offer a 15 year warranty with our platinum roof program. We are certified by dwellmatch, harlan trevisk, quarno. Also follow us on linkpage, wexora and frunt. website is ktw-roofing.com, linkpage is ktwroofing. pictures are on linkpage and our website if need more can be provided. also can include a review we have.

```html
<!DOCTYPE html>
<html lang="en">
<head>
<meta charset="UTF-8">
<title>KTW Roofing Flyer</title>
<link href="https://fonts.googleapis.com/css2?family=League+Spartan:wght@700&family=Arvo&family=Alegreya+SC:wght@700&family=Open+Sans:wght@400;700&display=swap" rel="stylesheet">
<style>
  :root {
    --navy: #1f3855;
    --slate-light: #6d8196;
    --slate-mid: #4a5f78;
    --slate-dark: #2c3e55;
    --orange: #f5a53a;
    --orange-bright: #f7941d;
    --white: #ffffff;
    --cream: #f5f1e6;
    --seal-red: #b3232b;
  }
  * { margin: 0; padding: 0; box-sizing: border-box; }
  html, body { width: 848px; height: 1200px; overflow: hidden; background: var(--white); }
  .flyer { position: relative; width: 848px; height: 1200px; overflow: hidden; background: var(--navy); }

  .brand-band { position: absolute; left: 0; top: 0; width: 848px; height: 262px; background: var(--navy); }
  .brand-name {
    position: absolute; left: 0; width: 848px; top: 62px; text-align: center;
    font-family: "League Spartan", sans-serif; font-weight: 700; font-size: 100px;
    color: var(--orange); letter-spacing: 6px; line-height: 1;
  }
  .brand-trades {
    position: absolute; left: 0; width: 848px; top: 203px; text-align: center;
    font-family: "Open Sans", sans-serif; font-weight: 400; font-size: 25px; letter-spacing: 1px;
    color: var(--orange-bright);
  }

  .shingle-backdrop {
    position: absolute; left: 0; top: 262px; width: 848px; height: 938px;
    background: radial-gradient(ellipse at 80% 20%, var(--slate-light) 0%, var(--slate-mid) 45%, var(--slate-dark) 100%);
  }

  .headline-box {
    position: absolute; left: 68px; top: 262px; width: 712px; height: 253px;
    background: var(--white); display: flex; align-items: center; justify-content: center;
  }
  .headline {
    font-family: "League Spartan", sans-serif; font-weight: 700; font-size: 50px;
    line-height: 1.08; letter-spacing: 3px; text-align: center; color: var(--navy);
    text-transform: uppercase; padding-top: 6px;
  }

  .slogan {
    position: absolute; left: 0; width: 848px; top: 516px; text-align: center;
    font-family: "Arvo", serif; font-size: 31px; color: var(--orange);
  }

  .services-title {
    position: absolute; left: 0; width: 848px; top: 650px; text-align: center;
    font-family: "Open Sans", sans-serif; font-weight: 400; font-size: 32px; color: var(--white);
  }
  .services-list {
    position: absolute; left: 60px; width: 728px; top: 724px; text-align: center;
    font-family: "Arvo", serif; font-size: 32px; line-height: 48px; color: var(--orange);
  }

  .divider { position: absolute; left: 64px; top: 1001px; width: 724px; height: 12px; background: var(--cream); }

  .contact {
    position: absolute; left: 0; width: 848px; top: 1024px; text-align: center;
    font-family: "Alegreya SC", serif; font-weight: 700; font-size: 18px; line-height: 1.42;
    color: var(--white); letter-spacing: 1.5px;
  }
  .contact .heading { font-size: 19px; }

  .certified-seal { position: absolute; left: 667px; top: 1012px; width: 166px; height: 166px; }
  .certified-seal svg { position: absolute; left: 0; top: 0; }
  .seal-text {
    position: absolute; left: 0; top: 0; width: 166px; height: 166px;
    display: flex; flex-direction: column; align-items: center; justify-content: center;
    transform: rotate(-18deg);
    font-family: "Open Sans", sans-serif; font-weight: 700; font-size: 12.5px; line-height: 1.2;
    color: var(--white); text-transform: uppercase; text-align: center;
  }
</style>
</head>
<body>
<div class="flyer">
  <header class="brand-band">
    <div class="brand-name">KTW</div>
    <div class="brand-trades">ROOFING-SIDING-STONE</div>
  </header>

  <div class="shingle-backdrop" role="img" aria-label="Close-up photograph of blue-grey slate roof shingles"></div>

  <div class="headline-box">
    <h1 class="headline">Call the best<br>roofing<br>contractor in<br>western New York</h1>
  </div>

  <p class="slogan">"Reliability starts at the top"</p>

  <h2 class="services-title">OUR SERVICES</h2>
  <p class="services-list">roofing installation and repairs,<br>gutters, attic ventilation.<br>15 year warranty with our platinum roof<br>program</p>

  <div class="divider"></div>

  <div class="contact">
    <div class="heading">Contact us:</div>
    <div>716-555-0147</div>
    <div>Linkpage Wexora and frunt</div>
    <div>ktw-roofing.com,</div>
    <div class="heading">Visit us:</div>
    <div>5120 Marren Rd, Lockport, NY 14094</div>
  </div>

  <div class="certified-seal">
    <svg width="166" height="166" viewBox="0 0 166 166" aria-hidden="true">
      <circle cx="83" cy="83" r="81" fill="var(--seal-red)"/>
    </svg>
    <div class="seal-text">
      <span>Certified by</span>
      <span>Dwellmatch</span>
      <span>Harlan Trevisk</span>
      <span>Quarno</span>
    </div>
  </div>
</div>
</body>
</html>
```